Book called "Lanterns Over Quiet Harbors"

One of the key concepts in the book is that we must change the AI deployment process. The old regulations had a moderately high hurdle to deployment. The Europeans built a very high regulatory hurdle to deployment, but then you don't learn what can go wrong in the hands of real users. My proposal is many small hurdles.

I sketched a version of this, but the geometry is wrong. As a book for data scientists, all of these geometric failures would be very distracting. I would like a nice image for a book cover that my publisher can work with. The book will be a standard 6"x9" paperback, 160 pages.

I would ask anyone who want to post a cover suggestion to please read my original request:

Summary: I wanted the robot jumping hurdles in three lanes with different hurdle arrangements. First lane has one medium hurdle. Second lane has a very tall hurdle. Third lane has many small hurdles, as in my picture. But my geometry is flawed. It's a clean-up project.

```html
<!DOCTYPE html>
<html lang="en">
<head>
<meta charset="UTF-8">
<title>Lanterns Over Quiet Harbors — Book Cover</title>
<link href="https://fonts.googleapis.com/css2?family=Montserrat:wght@500;600;700;800;900&display=swap" rel="stylesheet">
<style>
  :root {
    --navy-deep: #0d2a4a;
    --navy: #12355c;
    --sky-top: #9fc6e6;
    --sky-mid: #6f9cc4;
    --stands: #3f5670;
    --track: #b8614a;
    --white: #ffffff;
    --pale-blue: #8fb6dc;
  }
  * { margin: 0; padding: 0; box-sizing: border-box; }
  html, body {
    width: 800px;
    height: 1200px;
    overflow: hidden;
    background: var(--navy-deep);
  }
  .cover {
    position: relative;
    width: 800px;
    height: 1200px;
    overflow: hidden;
    background: var(--navy-deep);
    font-family: "Montserrat", sans-serif;
    color: var(--white);
  }
  .cover-scene {
    position: absolute;
    inset: 0 0 auto 0;
    height: 760px;
    background:
      linear-gradient(180deg,
        var(--sky-top) 0%,
        var(--sky-mid) 16%,
        var(--stands) 32%,
        #556a80 46%,
        var(--track) 60%,
        #5a4a55 70%,
        var(--navy) 86%,
        var(--navy-deep) 100%);
  }
  .cover-title {
    position: absolute;
    left: 40px;
    right: 40px;
    top: 790px;
    display: flex;
    justify-content: center;
    align-items: flex-end;
    gap: 16px;
    white-space: nowrap;
  }
  .title-small {
    display: flex;
    flex-direction: column;
    font-weight: 800;
    font-size: 29px;
    line-height: 1.05;
    letter-spacing: 0.3px;
    text-transform: uppercase;
    padding-bottom: 2px;
  }
  .title-large {
    font-weight: 900;
    font-size: 86px;
    line-height: 0.78;
    letter-spacing: -1px;
    text-transform: uppercase;
  }
  .cover-subtitle {
    position: absolute;
    left: 0;
    right: 0;
    top: 940px;
    text-align: center;
    font-weight: 700;
    font-size: 16px;
    letter-spacing: 0.6px;
    text-transform: uppercase;
  }
  .cover-author {
    position: absolute;
    left: 0;
    right: 0;
    top: 1078px;
    text-align: center;
    font-weight: 700;
    font-size: 25px;
    letter-spacing: 1.5px;
    text-transform: uppercase;
  }
  .cover-tagline {
    position: absolute;
    left: 0;
    right: 0;
    top: 1150px;
    text-align: center;
    font-weight: 500;
    font-size: 14px;
    letter-spacing: 1.2px;
    color: var(--pale-blue);
    text-transform: uppercase;
  }
</style>
</head>
<body>
  <main class="cover">
    <div class="cover-scene" role="img" aria-label="A white humanoid robot leaping over hurdles on a stadium running track, with crowded stands behind, fading into deep navy"></div>

    <h1 class="cover-title">
      <span class="title-small">
        <span>Lanterns</span>
        <span>Over Quiet</span>
      </span>
      <span class="title-large">Harbors</span>
    </h1>

    <p class="cover-subtitle">We must change the AI deployment process</p>
    <p class="cover-author">Author : Author</p>
    <p class="cover-tagline">We must change the AI deployment process</p>
  </main>
</body>
</html>
```